Residential home builder needs a fresh looking business card

We require a fresh looking business card for our business. We like the clean modern look. I have uploaded out logo and our email footer that incorporates some different elements. Blacks and Whites are good but i will leave this up to the design crowd creative minds.

our slogan is:
your idea of the perfect home

website (temporary site) but similar look and feel to the finished one
pinegrovedwellings.com.au

We also have intentions to apply the same look and feel to the rest of our stationary (letterheads, envelopes, site signs, vehicles etc)

Home Builder

```html
<!DOCTYPE html>
<html lang="en">
<head>
<meta charset="utf-8">
<title>Pinegrove Dwellings – Business Card</title>
<link rel="stylesheet" href="https://fonts.googleapis.com/css2?family=Arimo:wght@400;700&display=swap">
<style>
  :root {
    --yellow: #f6df1c;
    --ink: #1a1a1a;
    --grey: #555555;
    --white: #ffffff;
    --stage: #e9e7e2;
  }
  * { margin: 0; padding: 0; box-sizing: border-box; }
  html, body { width: 1200px; height: 675px; overflow: hidden; }
  body {
    background: var(--stage);
    font-family: "Arimo", Arial, sans-serif;
    color: var(--ink);
    position: relative;
  }
  .card {
    position: absolute;
    top: 194px;
    width: 500px;
    height: 286px;
    box-shadow: 0 6px 18px rgba(0,0,0,0.12);
  }
  .card--front { left: 70px; background: var(--white); }
  .card--back { left: 630px; background: var(--yellow); display: flex; align-items: center; justify-content: center; }

  .brand { display: flex; align-items: center; gap: 10px; }
  .brand__mark { width: 16px; height: 16px; background: var(--ink); flex: none; }
  .card--front .brand__mark { background: var(--yellow); }
  .brand__name {
    font-weight: 700;
    font-size: 24px;
    letter-spacing: 0.5px;
    color: var(--ink);
    white-space: nowrap;
  }
  .card--back .brand__name { font-size: 30px; }

  .card--front .brand { position: absolute; left: 30px; top: 128px; }
  .card--front .brand__name { font-size: 20px; }

  .contact {
    position: absolute;
    left: 276px;
    top: 56px;
    width: 206px;
    font-size: 11px;
    line-height: 1.35;
    color: var(--grey);
  }
  .contact__name { color: var(--yellow); font-weight: 700; font-size: 15px; line-height: 1.1; }
  .contact__role { margin-bottom: 14px; }
  .contact__address { margin-bottom: 8px; }
  .contact__line { display: flex; align-items: center; gap: 7px; }
  .contact__line svg { width: 11px; height: 11px; flex: none; }
</style>
</head>
<body>

<section class="card card--front" aria-label="Business card front">
  <div class="brand">
    <span class="brand__mark"></span>
    <span class="brand__name">Pinegrove Dwellings</span>
  </div>

  <div class="contact">
    <p class="contact__name">Mark Ellison</p>
    <p class="contact__role">President CEO</p>
    <p class="contact__address">418 Harbour Rd,<br>Ste 12 Newport,<br>NSW 2106 Australia</p>
    <p class="contact__line">
      <svg viewBox="0 0 12 12" aria-hidden="true"><path fill="#f6df1c" d="M2.5 1h2l1 3-1.4 1a6 6 0 0 0 2.9 2.9l1-1.4 3 1v2a1.5 1.5 0 0 1-1.5 1.5A9.5 9.5 0 0 1 1 2.5 1.5 1.5 0 0 1 2.5 1z"/></svg>
      +61 (02) 5550 1842
    </p>
    <p class="contact__line">
      <svg viewBox="0 0 12 12" aria-hidden="true"><circle cx="6" cy="6" r="5.5" fill="#f6df1c"/><path d="M1 6h10M6 .5c-2 2.5-2 8.5 0 11M6 .5c2 2.5 2 8.5 0 11" stroke="#fff" stroke-width=".8" fill="none"/></svg>
      www.pinegrovedwellings.com.au
    </p>
  </div>
</section>

<section class="card card--back" aria-label="Business card back">
  <div class="brand">
    <span class="brand__mark"></span>
    <span class="brand__name">Pinegrove Dwellings</span>
  </div>
</section>

</body>
</html>
```